Women's Jewellery startup needs a captivating, beautifully designed and intuitive online store

[12/24 update]

Added 2 additional documents:

Feedback on designs received so far: designer feedback.docx
Product images from catalogue: products images.docx

Please read the feedback provided on designs provided so far to guide you further on your submission. The product images can be used to create promotional banners for the site.

@@@Added a document (VELISSE JEWELLERY_checklist.docx) which can be used by designers as a checklist when submitting their designs to ensure all aspects of the requirements have been covered @@@

+++IMPORTANT BUT NOT SPECIFIED IN THE REQUIREMENTS DOCUMENT - DESIGN SHOULD INCLUDE SUPPORT FOR MOBILE FRIENDLY SITE TOO+++

***Previous experience designing Jewellery online stores preferred (not essential)***

The name of the online Jewellery store is "Velisse Jewellery" and the business is based in Hong Kong. It will be run by 2 stay at home mothers. We need a Shopify themed store designed that will achieve the following objectives in order of priority:

• Conversion: The primary objective of the design/content is to prompt the customer to make a purchase. While this may sound obvious, it is mentioned so as not to distract the design process by focusing on other objectives (which are also important). The site also needs to be optimized so as to rank high in search engine searches for relevant keywords (SEO)
• Navigation: An intuitive interface which takes away a lot of the thinking from the customer by making it obvious what they need to do when they visit the store
• Engagement: Encourages the customer to spend time on the website and share content with their social network

Where applicable, the design of the store should reflect as closely as possible the mission statements and words outlined below:

• Jewellery you’ll fall in love with
• We want every client to leave the store with a smile
• We want to be able to provide the best service we can in every situation no matter what
• We aim to increase our business by word of mouth; therefore we tell people things about our store that makes it interesting for them to share
• We love every customer, no matter how difficult things get
• We, as a team, are so well informed about our products and brands that we always have the best information for our customers
• We celebrate women here!
• We celebrate life in here!
• We celebrate beauty here!
• We celebrate families here, as jewellery often stays within families.
• We will always try to make an extra step
• We will always try to exceed the expectation of our customers
• We will go as far as we possibly can to attract a customer back to our store and connect with us
• Every client that leaves our store knows more about jewellery because we passionately told him about it
• Romantic, classic, love, warm, cool, stylish

A draft functional specification is attached with this brief. We would like the design to reflect as closely as possible the functional requirements outlined in the document. Open to suggestions to improve upon the functional requirements.

Target Market(s)

Women aged 18-55

Industry/Entity Type

Jewelry Store

Coding

Coded - Design and coding required

Number of Pages Required

5+ page

Font styles to use
Other font styles liked:
• Myriad Pro as per Logo but open to any font that complements this one

Requirements
Must have
• 1. A look that encourages the user to make a purchase
• 2. An intuitive, easy to navigate and engaging interface
• 3. Primary colour scheme as defined in the functional specification attached
• 4. Simplistic look, not too cluttered
Nice to have
• 1. Closely matching the functional requirements of the site as outlined in the requirements specification but open to any better ideas

```html
<!DOCTYPE html>
<html lang="en">
<head>
<meta charset="utf-8">
<title>Velisse Jewellery – Desktop and Mobile Home</title>
<link href="https://fonts.googleapis.com/css2?family=Libre+Baskerville:wght@400;700&family=Roboto:wght@400;500;700&display=swap" rel="stylesheet">
<style>
:root{
  --gold:#c99a45;
  --ink:#222;
  --muted:#555;
  --light:#eeeeee;
  --line:#d6d6d6;
  --stage:#ececec;
  --white:#fff;
}
*{box-sizing:border-box;margin:0;padding:0}
html,body{width:940px;height:1200px;overflow:hidden}
body{background:var(--stage);font-family:'Roboto',sans-serif;color:var(--ink);position:relative}
.abs{position:absolute}
.page{position:absolute;background:var(--white);overflow:hidden;box-shadow:0 2px 10px rgba(0,0,0,.15)}
.desktop{left:34px;top:46px;width:588px;height:1110px}
.mobile{left:678px;top:108px;width:220px;height:1092px}

.topbar{position:absolute;left:0;top:0;width:100%;height:16px;background:var(--light);font-size:5px;color:var(--ink)}
.topbar span{position:absolute;top:5px;white-space:nowrap;line-height:6px}
.topbar svg{width:6px;height:6px;vertical-align:-1px;margin-right:2px}

.brand{position:absolute;text-align:center;font-family:'Libre Baskerville',serif;color:var(--gold)}
.brand .mark{display:block;margin:0 auto 2px;border-radius:50%;background:var(--gold)}
.brand .name{letter-spacing:2px;display:block}

.nav{position:absolute;font-size:5px;color:var(--ink);white-space:nowrap}
.search-box{position:absolute;height:12px;background:var(--light);font-size:4.5px;color:#444;padding-left:10px;line-height:12px}

.photo{position:absolute}
.hero-photo{background:
  linear-gradient(115deg,rgba(0,0,0,0) 42%,rgba(190,190,195,.35) 55%,rgba(0,0,0,0) 68%),
  radial-gradient(ellipse 45% 60% at 66% 48%,#9a9aa0 0%,#505055 35%,rgba(20,20,20,0) 75%),
  linear-gradient(180deg,#050505,#1a1a1a 60%,#0a0a0a)}
.hero-title{position:absolute;color:var(--white);font-family:'Libre Baskerville',serif;font-weight:700;line-height:1.15;white-space:nowrap}
.hero-sub{position:absolute;color:#eee;font-family:'Libre Baskerville',serif;line-height:1.45;white-space:nowrap}
.btn{position:absolute;border-radius:20px;font-family:'Libre Baskerville',serif;text-align:center;font-weight:700;letter-spacing:.3px;white-space:nowrap}
.btn-light{background:var(--white);color:var(--gold)}
.btn-gold{background:var(--gold);color:var(--white)}

.tile{position:absolute;overflow:hidden}
.tile-ruby{background:
  radial-gradient(ellipse 60% 30% at 55% 62%,rgba(214,150,120,.55),rgba(214,150,120,0) 70%),
  linear-gradient(160deg,#3d3436,#161314 75%)}
.tile-diamond{background:
  radial-gradient(ellipse 22% 45% at 30% 30%,rgba(220,220,230,.75),rgba(220,220,230,0) 75%),
  radial-gradient(ellipse 22% 45% at 70% 30%,rgba(220,220,230,.75),rgba(220,220,230,0) 75%),
  linear-gradient(180deg,#3a3a3a,#1a1a1a 55%,#4a4a4a)}
.tile-aqua{background:
  radial-gradient(ellipse 18% 55% at 78% 70%,rgba(212,170,90,.6),rgba(212,170,90,0) 75%),
  linear-gradient(90deg,#000 55%,#0c0a06)}
.tile h3{position:absolute;font-family:'Libre Baskerville',serif;font-weight:700;color:var(--white);letter-spacing:.3px}
.tile p{position:absolute;font-family:'Libre Baskerville',serif;color:#dcdcdc}
.pill{position:absolute;border:1px solid var(--white);border-radius:12px;color:var(--white);text-align:center;font-weight:500;white-space:nowrap}

.section-title{position:absolute;font-family:'Libre Baskerville',serif;font-weight:700;color:var(--ink);text-align:center;letter-spacing:.5px}
.section-title i{font-style:normal;color:#bbb;font-weight:400}

.product{position:absolute;border:1px solid var(--line);background:var(--white)}
.product .shot{position:absolute;left:12px;right:12px;top:10px;height:74px;border-radius:3px}
.shot-ring{background:radial-gradient(ellipse at 50% 50%,#e6e3ef,#f7f7fa 70%)}
.shot-gold{background:radial-gradient(ellipse at 50% 50%,#f1dfc0,#faf6ef 70%)}
.shot-drop{background:radial-gradient(ellipse at 50% 50%,#dcdcdc,#f7f7f7 70%)}
.shot-blue{background:radial-gradient(ellipse at 50% 50%,#dde1f3,#f7f8fc 70%)}
.product .name{position:absolute;font-weight:500;color:var(--ink)}
.product .meta{position:absolute;color:var(--muted)}
.product .price{position:absolute;color:var(--gold);font-weight:500}
.pager{position:absolute;text-align:center;color:var(--ink)}

.newsletter{position:absolute;left:0;width:100%;background:linear-gradient(135deg,#232323,#0f0f0f 50%,#252525)}
.newsletter h4{position:absolute;width:100%;text-align:center;color:var(--white);font-family:'Libre Baskerville',serif;font-weight:400;letter-spacing:.6px}
.email{position:absolute;background:var(--white);border-radius:14px}
.email span{position:absolute;color:#666;white-space:nowrap}
.social{position:absolute;display:flex}
.social b{display:flex;align-items:center;justify-content:center;border:1px solid #ccc;transform:rotate(45deg)}
.social b::after{content:"";width:4px;height:4px;border-radius:50%;background:#ddd}

.footer{position:absolute;left:0;width:100%;background:var(--light)}
.footer h5{position:absolute;font-family:'Libre Baskerville',serif;font-weight:700;color:var(--gold)}
.footer h6{position:absolute;font-family:'Libre Baskerville',serif;font-weight:700;color:var(--ink)}
.footer ul{position:absolute;list-style:none;color:#444}
.contact{position:absolute;display:flex;align-items:center;color:#333;line-height:1.3}
.contact .ico{flex:none;border:1px solid var(--gold);transform:rotate(45deg);display:flex;align-items:center;justify-content:center}
.contact .ico svg{transform:rotate(-45deg)}
.copyright{position:absolute;left:0;width:100%;border-top:1px solid #ccc;background:var(--light);font-size:5px;color:#333}
</style>
</head>
<body>

<main class="page desktop">
  <div class="topbar">
    <span style="left:98px"><svg viewBox="0 0 10 10"><circle cx="5" cy="3" r="2.2" fill="#222"/><path d="M1 10a4 4 0 0 1 8 0z" fill="#222"/></svg>Sign Up</span>
    <span style="left:130px"><b>$</b> Currency Selector</span>
    <span style="left:234px">Extra 10% off Diamond rings till March 31st, 2018</span>
    <span style="left:417px"><svg viewBox="0 0 10 10"><path d="M5 9 1 5a2.2 2.2 0 0 1 4-3 2.2 2.2 0 0 1 4 3z" fill="#222"/></svg>Wishlist</span>
    <span style="left:453px"><svg viewBox="0 0 10 10"><path d="M0 1h2l1.5 5h5L10 2H3" fill="none" stroke="#222"/><circle cx="4" cy="8.5" r="1" fill="#222"/><circle cx="8" cy="8.5" r="1" fill="#222"/></svg>Add to Cart</span>
  </div>

  <svg class="abs" style="left:98px;top:38px" width="8" height="8" viewBox="0 0 10 10"><path d="M5 1 0 5.5h1.5V10h2.5V7h2v3h2.5V5.5H10z" fill="#c99a45"/></svg>
  <div class="nav" style="left:115px;top:40px">About Us &nbsp;&nbsp; | &nbsp;&nbsp; Shopping &nbsp;&nbsp; | &nbsp;&nbsp; Customer Care</div>

  <div class="brand" style="left:244px;top:23px;width:100px">
    <span class="mark" style="width:14px;height:14px"></span>
    <span class="name" style="font-size:8px">VELISSE</span>
  </div>

  <div class="nav" style="left:369px;top:40px;font-size:5.5px">Search</div>
  <div class="search-box" style="left:395px;top:36px;width:94px">Enter Keyword
    <svg class="abs" style="right:4px;top:3px" width="6" height="6" viewBox="0 0 10 10"><circle cx="4" cy="4" r="3" fill="none" stroke="#222" stroke-width="1.4"/><path d="M6.3 6.3 9.5 9.5" stroke="#222" stroke-width="1.4"/></svg>
  </div>

  <div class="photo hero-photo" role="img" aria-label="Close-up of a diamond engagement ring on a black background" style="left:0;top:66px;width:588px;height:292px"></div>
  <h1 class="hero-title" style="left:98px;top:140px;font-size:28px">Every piece of jewelry<br>tells a story</h1>
  <p class="hero-sub" style="left:98px;top:211px;font-size:9.5px">Be real be yourself, carry a piece of natural<br>and real jewelry</p>
  <div class="btn btn-light" style="left:98px;top:261px;width:76px;height:22px;line-height:22px;font-size:5.5px">CONTACT US</div>
  <div class="btn btn-gold" style="left:189px;top:261px;width:105px;height:22px;line-height:22px;font-size:5.5px">SEE THE COLLECTION</div>
  <svg class="abs" style="left:288px;top:322px" width="12" height="16" viewBox="0 0 12 16"><path d="M6 0v11" stroke="#fff" stroke-width="1.2"/><path d="M1.5 9 6 15l4.5-6z" fill="#fff"/></svg>

  <div class="tile tile-ruby" role="img" aria-label="Rose gold bracelet with crystals" style="left:98px;top:390px;width:190px;height:172px">
    <h3 style="left:11px;top:16px;font-size:12px">RUBY</h3>
    <p style="left:12px;top:31px;font-size:6px">10K Rose Gold</p>
    <div class="pill" style="left:110px;top:140px;width:58px;height:14px;line-height:12px;font-size:5px">VIEW COLLECTION</div>
  </div>
  <div class="tile tile-diamond" role="img" aria-label="Pair of diamond stud earrings" style="left:300px;top:390px;width:190px;height:84px">
    <h3 style="left:8px;top:56px;font-size:12px">DIAMOND</h3>
    <p style="left:8px;top:71px;font-size:6px">10K Rose Gold</p>
    <div class="pill" style="left:126px;top:58px;width:54px;height:14px;line-height:12px;font-size:5px">SHOP NOW</div>
  </div>
  <div class="tile tile-aqua" role="img" aria-label="Gold chain necklace with ring pendant" style="left:300px;top:479px;width:190px;height:83px">
    <h3 style="left:8px;top:11px;font-size:12px">AQUAMARINE</h3>
    <p style="left:8px;top:26px;font-size:6px">10K Rose Gold</p>
    <div class="pill" style="left:8px;top:47px;width:56px;height:14px;line-height:12px;font-size:4.5px">SHOP NECKLACE</div>
  </div>

  <h2 class="section-title" style="left:0;top:593px;width:588px;font-size:12px"><i>◁</i>&nbsp; NEW PRODUCTS &nbsp;<i>▷</i></h2>

  <div class="product" style="left:98px;top:628px;width:94px;height:124px">
    <div class="shot shot-ring" role="img" aria-label="Silver ring set with coloured gems"></div>
    <div class="name" style="left:7px;top:94px;font-size:6.5px">Rings</div>
    <div class="meta" style="left:7px;top:104px;font-size:5.5px">10K Rose Gold</div>
    <div class="price" style="left:7px;top:113px;font-size:6px">$220.00</div>
  </div>
  <div class="product" style="left:197px;top:628px;width:94px;height:124px">
    <div class="shot shot-gold" role="img" aria-label="Gold ring with red stone"></div>
    <div class="name" style="left:7px;top:94px;font-size:6.5px">Bracelets</div>
    <div class="meta" style="left:7px;top:104px;font-size:5.5px">14K Gold Rose</div>
    <div class="price" style="left:7px;top:113px;font-size:6px">$220.00</div>
  </div>
  <div class="product" style="left:296px;top:628px;width:94px;height:124px">
    <div class="shot shot-drop" role="img" aria-label="Silver drop earrings with dark stones"></div>
    <div class="name" style="left:7px;top:94px;font-size:6.5px">Earrings</div>
    <div class="meta" style="left:7px;top:104px;font-size:5.5px">10K Yellow Gold</div>
    <div class="price" style="left:7px;top:113px;font-size:6px">$220.00</div>
  </div>
  <div class="product" style="left:395px;top:628px;width:94px;height:124px">
    <div class="shot shot-blue" role="img" aria-label="Silver necklace with blue sapphire pendant"></div>
    <div class="name" style="left:7px;top:94px;font-size:6.5px">Necklaces</div>
    <div class="meta" style="left:7px;top:104px;font-size:5.5px">Gold plated</div>
    <div class="price" style="left:7px;top:113px;font-size:6px">$220.00</div>
  </div>
  <div class="pager" style="left:0;top:769px;width:588px;font-size:9px">&lt; / &gt;</div>

  <section class="newsletter" style="top:811px;height:133px">
    <h4 style="top:28px;font-size:12px">SUBSCRIBE NEWSLETTER</h4>
    <div class="email" style="left:177px;top:58px;width:228px;height:21px">
      <svg class="abs" style="left:15px;top:7px" width="9" height="7" viewBox="0 0 10 8"><rect x=".5" y=".5" width="9" height="7" fill="none" stroke="#c99a45"/><path d="M.5.5 5 4.5 9.5.5" fill="none" stroke="#c99a45"/></svg>
      <span style="left:34px;top:4px;font-size:5px;border-left:1px solid #ddd;padding-left:8px;line-height:13px">ENTER YOUR E-MAIL ADDRESS</span>
      <svg class="abs" style="right:10px;top:7px" width="8" height="7" viewBox="0 0 10 8"><path d="M0 4h8M5 1l3 3-3 3" fill="none" stroke="#111" stroke-width="1.3"/></svg>
    </div>
    <div class="social" role="img" aria-label="Social media links" style="left:262px;top:94px;gap:13px">
      <b style="width:14px;height:14px"></b><b style="width:14px;height:14px"></b><b style="width:14px;height:14px"></b>
    </div>
  </section>

  <footer class="footer" style="top:944px;height:142px">
    <h5 style="left:98px;top:28px;font-size:9.5px">Velisse Jewellery</h5>
    <div class="contact" style="left:100px;top:56px;font-size:5.5px;gap:10px">
      <span class="ico" style="width:14px;height:14px"><svg width="7" height="7" viewBox="0 0 10 10"><path d="M2 0 4 3 3 4.5A6 6 0 0 0 5.5 7L7 6l3 2-1 2C4 10 0 6 0 1z" fill="#c99a45"/></svg></span>+852 5550 1234</div>
    <div class="contact" style="left:100px;top:80px;font-size:5.5px;gap:10px">
      <span class="ico" style="width:14px;height:14px"><svg width="7" height="7" viewBox="0 0 10 10"><path d="M5 10C2 6 1.5 4.8 1.5 3.5a3.5 3.5 0 0 1 7 0C8.5 4.8 8 6 5 10z" fill="#c99a45"/><circle cx="5" cy="3.5" r="1.2" fill="#eee"/></svg></span>Lorem Ipsum is simply dummy<br>of the printing</div>
    <div class="contact" style="left:100px;top:110px;font-size:5.5px;gap:10px">
      <span class="ico" style="width:14px;height:14px"><svg width="7" height="6" viewBox="0 0 10 8"><rect x=".5" y=".5" width="9" height="7" fill="none" stroke="#c99a45"/><path d="M.5.5 5 4.5 9.5.5" fill="none" stroke="#c99a45"/></svg></span>hello@velissejewellery.com</div>

    <h6 style="left:249px;top:33px;font-size:7.5px">About Us</h6>
    <ul style="left:249px;top:58px;font-size:5px;line-height:11.5px"><li>Our Story</li><li>Wholesale inquiries</li></ul>
    <h6 style="left:349px;top:33px;font-size:7.5px">Shopping</h6>
    <ul style="left:349px;top:58px;font-size:5px;line-height:11.5px"><li>Orders</li><li>Wishlist</li><li>Size Guide</li></ul>
    <h6 style="left:429px;top:33px;font-size:7.5px">Customer Care</h6>
    <ul style="left:429px;top:58px;font-size:5px;line-height:11.5px"><li>Returns</li><li>FAQ's</li><li>Care &amp; Warranty</li><li>Contact Us</li></ul>
  </footer>
  <div class="copyright" style="top:1086px;height:24px">
    <span class="abs" style="left:98px;top:9px">© Copyright 2017 Velisse Jewellery. All Rights Reserved.</span>
    <span class="abs" style="left:453px;top:9px">Privacy Policy</span>
  </div>
</main>

<main class="page mobile">
  <div class="topbar"><span style="left:0;width:100%;text-align:center;font-size:4.5px">Extra 10% off Diamond rings till March 31st, 2018</span></div>
  <svg class="abs" style="left:9px;top:33px" width="7" height="7" viewBox="0 0 10 10"><path d="M5 1 0 5.5h1.5V10h2.5V7h2v3h2.5V5.5H10z" fill="#c99a45"/></svg>
  <svg class="abs" style="left:20px;top:34px" width="8" height="6" viewBox="0 0 10 8"><path d="M0 1h10M0 4h10M0 7h10" stroke="#222" stroke-width="1.2"/></svg>
  <div class="brand" style="left:70px;top:20px;width:80px">
    <span class="mark" style="width:13px;height:13px"></span>
    <span class="name" style="font-size:6.5px">VELISSE</span>
  </div>
  <div class="nav" style="left:180px;top:35px;font-size:5px">Search</div>
  <svg class="abs" style="left:207px;top:35px" width="6" height="6" viewBox="0 0 10 10"><circle cx="4" cy="4" r="3" fill="none" stroke="#222" stroke-width="1.4"/><path d="M6.3 6.3 9.5 9.5" stroke="#222" stroke-width="1.4"/></svg>

  <div class="photo hero-photo" role="img" aria-label="Close-up of a diamond engagement ring on a black background" style="left:0;top:60px;width:220px;height:188px"></div>
  <h1 class="hero-title" style="left:13px;top:114px;font-size:15px">Every piece of jewelry<br>tells a story</h1>
  <p class="hero-sub" style="left:13px;top:155px;font-size:5.5px">Be real be yourself, carry a piece of natural<br>and real jewelry</p>
  <div class="btn btn-light" style="left:13px;top:183px;width:45px;height:13px;line-height:13px;font-size:3.5px">CONTACT US</div>
  <div class="btn btn-gold" style="left:67px;top:183px;width:63px;height:13px;line-height:13px;font-size:3.5px">SEE THE COLLECTION</div>
  <svg class="abs" style="left:131px;top:224px" width="8" height="11" viewBox="0 0 12 16"><path d="M6 0v11" stroke="#fff" stroke-width="1.2"/><path d="M1.5 9 6 15l4.5-6z" fill="#fff"/></svg>

  <div class="tile tile-ruby" role="img" aria-label="Rose gold bracelet with crystals" style="left:15px;top:280px;width:190px;height:173px">
    <h3 style="left:11px;top:16px;font-size:12px">RUBY</h3>
    <p style="left:12px;top:31px;font-size:6px">10K Rose Gold</p>
    <div class="pill" style="left:112px;top:140px;width:58px;height:15px;line-height:13px;font-size:5px">VIEW COLLECTION</div>
  </div>
  <div class="tile tile-diamond" role="img" aria-label="Pair of diamond stud earrings" style="left:15px;top:466px;width:190px;height:84px">
    <h3 style="left:8px;top:56px;font-size:12px">DIAMOND</h3>
    <p style="left:8px;top:71px;font-size:6px">10K Rose Gold</p>
    <div class="pill" style="left:126px;top:58px;width:54px;height:14px;line-height:12px;font-size:5px">SHOP NOW</div>
  </div>
  <div class="tile tile-aqua" role="img" aria-label="Gold chain necklace with ring pendant" style="left:15px;top:562px;width:190px;height:84px">
    <h3 style="left:8px;top:11px;font-size:12px">AQUAMARINE</h3>
    <p style="left:8px;top:27px;font-size:6px">10K Rose Gold</p>
    <div class="pill" style="left:8px;top:47px;width:56px;height:14px;line-height:12px;font-size:4.5px">SHOP NECKLACE</div>
  </div>

  <h2 class="section-title" style="left:0;top:675px;width:220px;font-size:10px"><i>◁</i>&nbsp; NEW PRODUCTS &nbsp;<i>▷</i></h2>
  <div class="product" style="left:61px;top:706px;width:94px;height:124px">
    <div class="shot shot-ring" role="img" aria-label="Silver ring set with coloured gems"></div>
    <div class="name" style="left:9px;top:94px;font-size:6.5px">Rings</div>
    <div class="meta" style="left:9px;top:104px;font-size:5.5px">10K Rose Gold</div>
    <div class="price" style="left:9px;top:113px;font-size:6px">$220.00</div>
  </div>
  <div class="pager" style="left:0;top:842px;width:220px;font-size:9px">&lt; / &gt;</div>

  <section class="newsletter" style="top:884px;height:128px">
    <h4 style="top:26px;font-size:9.5px">SUBSCRIBE NEWSLETTER</h4>
    <div class="email" style="left:14px;top:53px;width:192px;height:18px">
      <svg class="abs" style="left:12px;top:6px" width="8" height="6" viewBox="0 0 10 8"><rect x=".5" y=".5" width="9" height="7" fill="none" stroke="#c99a45"/><path d="M.5.5 5 4.5 9.5.5" fill="none" stroke="#c99a45"/></svg>
      <span style="left:28px;top:3px;font-size:4px;border-left:1px solid #ddd;padding-left:6px;line-height:12px">ENTER YOUR E-MAIL ADDRESS</span>
      <svg class="abs" style="right:9px;top:6px" width="7" height="6" viewBox="0 0 10 8"><path d="M0 4h8M5 1l3 3-3 3" fill="none" stroke="#111" stroke-width="1.3"/></svg>
    </div>
    <div class="social" role="img" aria-label="Social media links" style="left:84px;top:85px;gap:11px">
      <b style="width:13px;height:13px"></b><b style="width:13px;height:13px"></b><b style="width:13px;height:13px"></b>
    </div>
  </section>

  <footer class="footer" style="top:1012px;height:80px">
    <h5 style="left:15px;top:24px;font-size:9.5px">Velisse Jewellery</h5>
    <div class="contact" style="left:17px;top:52px;font-size:5.5px;gap:10px">
      <span class="ico" style="width:14px;height:14px"><svg width="7" height="7" viewBox="0 0 10 10"><path d="M2 0 4 3 3 4.5A6 6 0 0 0 5.5 7L7 6l3 2-1 2C4 10 0 6 0 1z" fill="#c99a45"/></svg></span>+852 5550 1234</div>
    <div class="contact" style="left:17px;top:78px;font-size:5.5px;gap:10px">
      <span class="ico" style="width:14px;height:14px"><svg width="7" height="7" viewBox="0 0 10 10"><path d="M5 10C2 6 1.5 4.8 1.5 3.5a3.5 3.5 0 0 1 7 0C8.5 4.8 8 6 5 10z" fill="#c99a45"/></svg></span>Lorem Ipsum is simply dummy</div>
  </footer>
</main>

</body>
</html>
```